Label design - Superfood blend

We are a family owned nutrition company with big ambitions. Our goal is to develop a range of 100% natural supplements for women, inspired by nature & modern technology that helps them meet their nutritional needs while nourishing them from within. All our products are junk free because we believe that that’s how nature intended it. We also produce products through a sustainable process and only use biodegradable packaging for our products (See link - https://www.pouchwerk.example.uk/biodegradable-stand-pouch-250g-kraft)

Our brand style is modern and minimalist. This same style will be reflected in our social media, website and we want it to be represented through the label designs for our product packaging.

We want some creative designers to design a label that is true to our style (See attached packaging brief with designs we like) and displays our values of Premium, High Quality, Organic Real Food supplements focused on women. I have provided examples in the attached brief, but please only use as inspiration, I dont want any of them to be copied (sorry have had my fingers burnt already !)

Need extra days to review

Hello all, Please note this design is for a LABEL and not the whole package. We will have a 500gm biodegradable brown package, and we will have a label (which is what this project is about) that will be stuck on the front. The size of the label will be a rectangle (unless you come up with a new shape) in the size 20cm * 15cm. Please do not submit designs for the WHOLE from of the package, as we dont intend to have printed packages. Regards

Hello all, I have added a new logo version to the attachments, could you please also try that version. Could you also please look at the new sliders. We are only looking for a minimlaist theme. If you dont know what that means, please do feel free to ask, I would be happy to supply examples. Minimalist designs, means clean, modern, upmarket, elegant designs. It does not use too many colors and mostly sticks to a combination of black and white with colors used sparingly. See some below for your reference anyway. https://www.artbidhub.example.uk/design/48120573 https://www.artbidhub.example.uk/design/52961804 https://www.artbidhub.example.uk/design/47305916 https://www.artbidhub.example.uk/design/46719258 https://www.snapboardly.example.com/search/pins/?q=minimalist%20label%20design&rs=rs&eq=&etslf=2809&term_meta[]=minimalist%7Crecentsearch%7Cundefined&term_meta[]=label%7Crecentsearch%7Cundefined&term_meta[]=design%7Crecentsearch%7Cundefined Regards

Target Market(s)

The target market is women between the age 25 to 45, based in UK (mostly based in larger cities in UK). They are typically middle class or higher and would be in demanding jobs and social lives, that requires for them to meet their nutrition needs in convenient, easy to take forms. The women would also be socially conscious and sensitive to issues like women's rights, environmental issues, healthy food, organic food and sustainability etc. I have a much more detailed customer avatar if required

Font styles to use
Serif
Sans Serif
Decorative
Script

Colors
e8e8e8
474747
1b1b1b
add136

Requirements
Must have
• The label, should look minimalist and modern, throw in some out of the box creativity and we have a winner. Creativity will definitely be of importance. Our packaging is a biodegradable brown paper stand up pouch (Example link in product description). So to make it standout from other colorful packaging - being creative would definitely help.
• Please use the color schemes provided in the brief (See attachments). But if you want to experiment I would be open to it, as long as they are still minimalist and does not stray very far from the color given in the brief :)

```html
<!DOCTYPE html>
<html lang="en">
<head>
<meta charset="utf-8">
<title>Verdalune – Tend Thy Root label</title>
<link rel="stylesheet" href="https://fonts.googleapis.com/css2?family=Archivo:wght@800&family=Montserrat:wght@400;500&family=Roboto+Mono:wght@500&display=swap">
<style>
  :root {
    --bg: #f2f2f2;
    --label: #fbfbf9;
    --green: #1c9a40;
    --green-deep: #137a30;
    --fern: #e6e7d6;
    --ink: #474747;
    --ring: #8a8a80;
  }
  * { box-sizing: border-box; margin: 0; padding: 0; }
  html, body { width: 1200px; height: 800px; overflow: hidden; }
  body { background: var(--bg); position: relative; font-family: "Montserrat", sans-serif; }

  .label {
    position: absolute; left: 430px; top: 50px;
    width: 340px; height: 700px;
    background: var(--label);
    clip-path: polygon(0 0, 100% 0, 100% 93%, 93% 100%, 7% 100%, 0 93%);
    box-shadow: 0 2px 10px rgba(0,0,0,.08);
  }
  .label-frame { position: absolute; inset: 0; }

  .crown-leaf {
    position: absolute; left: 58px; top: 0; width: 224px; height: 140px;
    background: linear-gradient(180deg, var(--green) 0%, var(--green-deep) 100%);
    clip-path: polygon(0 0, 100% 0, 78% 45%, 50% 100%, 22% 45%);
  }
  .fern { position: absolute; background: linear-gradient(160deg, var(--fern), rgba(230,231,214,.35)); border-radius: 50% 50% 50% 50% / 60% 60% 40% 40%; }
  .fern--left-top { left: 6px; top: 80px; width: 70px; height: 190px; transform: rotate(-12deg); }
  .fern--right-top { right: 10px; top: 40px; width: 46px; height: 150px; transform: rotate(10deg); }
  .fern--left-mid { left: 4px; top: 330px; width: 40px; height: 140px; }
  .fern--right-low { right: 18px; top: 400px; width: 70px; height: 200px; transform: rotate(16deg); }

  .brand-seal {
    position: absolute; left: 70px; top: 180px; width: 200px; height: 200px;
    border: 1.5px solid var(--ring); border-radius: 50%;
    box-shadow: inset 0 0 0 5px var(--label), inset 0 0 0 6px #c9c9c0;
    background: var(--label);
    display: flex; align-items: center; justify-content: center;
  }
  .brand-name { font-size: 20px; letter-spacing: 3px; color: var(--ink); font-weight: 400; }

  .product-title {
    position: absolute; left: 36px; top: 392px;
    padding-left: 18px; border-left: 9px solid var(--green);
    font-family: "Archivo", sans-serif; font-weight: 800;
    font-size: 38px; line-height: 36px; color: var(--green);
  }
  .product-facts { position: absolute; left: 36px; top: 512px; list-style: none; font-family: "Roboto Mono", monospace; font-size: 12px; color: var(--green); line-height: 16px; }
  .product-facts li { position: relative; padding-left: 18px; margin-bottom: 6px; }
  .product-facts li::before { content: ""; position: absolute; left: 0; top: 4px; width: 8px; height: 8px; border-radius: 50%; background: var(--green); }

  .badges { position: absolute; left: 56px; top: 580px; display: flex; gap: 26px; }
  .badge { width: 46px; height: 46px; border-radius: 50%; border: 2px solid #555; }
  .badge--vegan { border-color: var(--green); }

  .net-weight { position: absolute; left: 56px; top: 670px; font-family: "Roboto Mono", monospace; font-size: 10px; color: var(--green); }
  .net-weight .unit { margin-left: 60px; }
</style>
</head>
<body>
  <article class="label">
    <svg class="label-frame" width="340" height="700" viewBox="0 0 340 700" aria-hidden="true">
      <polygon points="14,14 326,14 326,650 286,686 54,686 14,650" fill="none" stroke="#1c9a40" stroke-width="2"/>
    </svg>
    <div class="fern fern--left-top" role="img" aria-label="Faint fern leaf decoration"></div>
    <div class="fern fern--right-top" role="img" aria-label="Faint fern leaf decoration"></div>
    <div class="fern fern--left-mid" role="img" aria-label="Faint fern leaf decoration"></div>
    <div class="fern fern--right-low" role="img" aria-label="Faint fern leaf decoration"></div>
    <div class="crown-leaf" role="img" aria-label="Large green leaf illustration hanging from the top edge"></div>

    <div class="brand-seal"><span class="brand-name">VERDALUNE</span></div>

    <h1 class="product-title">TEND<br>THY<br>ROOT</h1>
    <ul class="product-facts">
      <li>Organic, Plant-Based Prebiotics<br>and Superfood Blend</li>
      <li>Food Supplement</li>
    </ul>

    <div class="badges">
      <span class="badge badge--organic" role="img" aria-label="Organic certification badge"></span>
      <span class="badge badge--vegan" role="img" aria-label="Vegan certification badge"></span>
    </div>

    <p class="net-weight">NET Weight :<span class="unit">GM</span></p>
  </article>
</body>
</html>
```